Aged Care Home - TM

We need a website design for a homepage and a content page for an aged care home in Brisbane. I have attached a detailed design/content brief and their logo to be used in concepts. Also bear in mind this design will be skinned for Dot Net Nuke 4.8.2 so design needs to be used on this content management system.

The following elements are required in the design:

• Phone number will be featured in banner on each page 07 5281 6637

• An area for a large flash banner of rotating images on homepage

• Images need to reflect credibility, professionalism and caring (just use some example images for now as we’ll need to source some)

• Large logo in banner as well

• Some icons on homepage to include:

• Download Application Form

• Admission Kit

• Contact Us

```html
<!DOCTYPE html>
<html lang="en">
<head>
<meta charset="utf-8">
<title>The TM Home – Website Concepts</title>
<link rel="stylesheet" href="https://fonts.googleapis.com/css2?family=Arimo:wght@400;700&family=Caveat:wght@500&display=swap">
<style>
  :root {
    --backdrop: #d0c9dc;
    --white: #ffffff;
    --ink: #222222;
    --grey-text: #555555;
    --navy: #2e2470;
    --heading: #3d2e7a;
    --nav: #7b65b3;
    --dark: #36304f;
    --button: #7b65b3;
    --button-light: #9b82e0;
    --panel: #f5f5f5;
    --sidebar: #f5f2fd;
    --link: #6a57b0;
    --photo-a: #6b4a3a;
    --photo-b: #c9987c;
    --photo-c: #3c2e3a;
  }
  * { box-sizing: border-box; margin: 0; padding: 0; }
  html, body { width: 1200px; height: 2400px; overflow: hidden; }
  body { background: var(--backdrop); font-family: "Arimo", Arial, sans-serif; color: var(--ink); position: relative; }

  .page { position: absolute; left: 57px; width: 1092px; background: var(--white); border-radius: 0 22px 18px 18px; overflow: hidden; }
  .page--home { top: 108px; height: 1056px; }
  .page--content { top: 1371px; height: 931px; }

  .site-header { position: absolute; top: 0; left: 0; width: 100%; height: 141px; }
  .brand { position: absolute; left: 38px; top: 40px; display: flex; align-items: center; gap: 14px; }
  .brand-mark { width: 22px; height: 22px; background: var(--nav); }
  .brand-name { font-size: 24px; font-weight: 400; color: var(--navy); letter-spacing: 0.5px; }
  .phone { position: absolute; right: 30px; top: 34px; display: flex; align-items: center; gap: 12px; font-size: 25px; font-weight: 700; color: var(--dark); letter-spacing: 1px; }
  .utility-links { position: absolute; right: 14px; top: 112px; font-size: 12px; color: var(--ink); word-spacing: 3px; }

  .main-nav { position: absolute; top: 141px; left: 0; width: 100%; height: 46px; display: flex; background: var(--nav); }
  .main-nav a { display: flex; align-items: center; justify-content: center; color: var(--white); font-size: 14.5px; text-decoration: none; }
  .main-nav a.is-current { background: var(--dark); }
  .main-nav .newsletter { background: linear-gradient(#ffffff, #e4e1ea); color: var(--dark); font-family: "Caveat", cursive; font-size: 25px; }

  .hero { position: absolute; top: 187px; left: 0; width: 100%; background: var(--dark); }
  .page--home .hero { height: 396px; }
  .page--content .hero { height: 228px; }
  .hero-photo { position: absolute; left: 29px; width: 854px; background: linear-gradient(110deg, var(--photo-c) 0%, var(--photo-a) 30%, var(--photo-b) 60%, var(--photo-a) 100%); }
  .page--home .hero-photo { top: 26px; height: 339px; }
  .page--content .hero-photo { top: 24px; height: 178px; }
  .hero-caption { position: absolute; left: 29px; top: 266px; width: 580px; height: 99px; background: rgba(54, 48, 79, 0.65); color: var(--white); font-size: 31px; letter-spacing: 1px; padding: 36px 0 0 46px; }

  .quick-links { position: absolute; right: 27px; width: 172px; }
  .quick-link { position: absolute; left: 0; width: 172px; display: flex; align-items: center; gap: 16px; padding-left: 16px; background: var(--button); color: var(--white); font-size: 14px; line-height: 1.3; text-decoration: none; }
  .quick-link.is-primary { background: var(--button-light); }
  .quick-link svg { flex: none; }
  .page--home .quick-links { top: 26px; }
  .page--home .quick-link { height: 99px; }
  .page--home .quick-link:nth-child(1) { top: 0; }
  .page--home .quick-link:nth-child(2) { top: 120px; }
  .page--home .quick-link:nth-child(3) { top: 240px; }
  .page--content .quick-links { top: 24px; right: 29px; }
  .page--content .quick-link { height: 58px; border-bottom: 2px solid var(--dark); }
  .page--content .quick-link:nth-child(1) { top: 0; }
  .page--content .quick-link:nth-child(2) { top: 60px; }
  .page--content .quick-link:nth-child(3) { top: 120px; border-bottom: 0; }

  .content-area { position: absolute; left: 0; width: 100%; }
  .page--home .content-area { top: 583px; height: 440px; }
  .page--content .content-area { top: 415px; height: 485px; }
  .sidebar { position: absolute; top: 0; right: 0; width: 334px; height: 100%; background: var(--sidebar); }
  .sidebar-title { position: absolute; left: 42px; font-size: 22px; font-weight: 400; color: var(--heading); }
  .page--home .sidebar-title { top: 22px; }
  .page--content .sidebar-title { top: 68px; }
  .room-card { position: absolute; left: 42px; width: 249px; height: 91px; background: var(--white); display: flex; gap: 10px; padding: 10px 6px; }
  .room-thumb { flex: none; width: 92px; height: 68px; background: linear-gradient(#b9c9dd 0%, #e8e4dc 55%, #6f8a55 100%); }
  .room-card a { color: var(--link); font-size: 14px; line-height: 1.25; }
  .view-more { position: absolute; right: 44px; font-size: 12px; color: var(--ink); }

  .intro-panel { position: absolute; left: 42px; width: 671px; background: var(--panel); }
  .page--home .intro-panel { top: 51px; height: 338px; text-align: center; padding: 50px 24px 0; }
  .intro-panel h1 { font-size: 29px; font-weight: 700; color: var(--heading); margin-bottom: 24px; }
  .intro-panel .welcome-text { font-size: 15.5px; line-height: 1.75; color: var(--grey-text); }
  .intro-panel .welcome-text + .welcome-text { margin-top: 22px; }

  .page--content .intro-panel { top: 34px; height: 367px; padding: 24px 40px 0 42px; }
  .section-title { display: flex; align-items: center; gap: 22px; margin-left: 0; margin-bottom: 34px; font-size: 27px; font-weight: 400; color: var(--heading); }
  .body-text { font-size: 14.5px; line-height: 1.22; color: var(--ink); }
  .body-text + .body-text { margin-top: 20px; }

  .site-footer { position: absolute; left: 0; bottom: 0; width: 100%; background: var(--dark); color: var(--white); font-size: 11.5px; padding-left: 38px; display: flex; align-items: center; }
  .page--home .site-footer { height: 33px; }
  .page--content .site-footer { height: 31px; }
</style>
</head>
<body>

<!-- Homepage -->
<section class="page page--home">
  <header class="site-header">
    <div class="brand"><span class="brand-mark"></span><span class="brand-name">THE TM HOME</span></div>
    <div class="phone">
      <svg width="24" height="24" viewBox="0 0 24 24"><path d="M6.6 10.8c1.4 2.8 3.8 5.1 6.6 6.6l2.2-2.2c.3-.3.7-.4 1-.2 1.1.4 2.3.6 3.6.6.6 0 1 .4 1 1V20c0 .6-.4 1-1 1C10.6 21 3 13.4 3 4c0-.6.4-1 1-1h3.5c.6 0 1 .4 1 1 0 1.3.2 2.5.6 3.6.1.3 0 .7-.2 1z" fill="#36304f"/></svg>
      07 5281 6637
    </div>
    <div class="utility-links">| Career Opportunity | &nbsp;Link &nbsp;| &nbsp;Contact Us &nbsp;|</div>
  </header>
  <nav class="main-nav">
    <a class="is-current" style="width:67px">Home</a>
    <a style="width:87px">About Us</a>
    <a style="width:146px">Accommodation</a>
    <a style="width:120px">Financial Info</a>
    <a style="width:158px">Philosophy of Care</a>
    <a style="width:108px">Contact Us</a>
    <a style="width:205px">Health &amp; Fitness Programs</a>
    <a class="newsletter" style="width:201px">Sign up for newsletter</a>
  </nav>
  <div class="hero">
    <div class="hero-photo" role="img" aria-label="Rotating banner photo of an elderly couple sharing an affectionate moment"></div>
    <div class="hero-caption">Alan &amp; Rose 2009</div>
    <div class="quick-links">
      <a class="quick-link is-primary">
        <svg width="22" height="26" viewBox="0 0 22 26"><path d="M2 1h12l6 6v18H2z" fill="none" stroke="#fff" stroke-width="2"/><path d="M11 9v9M7 14l4 4 4-4" fill="none" stroke="#fff" stroke-width="2"/></svg>
        <span>Download<br>Application Form</span>
      </a>
      <a class="quick-link">
        <svg width="22" height="26" viewBox="0 0 22 26"><path d="M2 1h12l6 6v18H2z" fill="none" stroke="#fff" stroke-width="2"/><path d="M6 14l4 4 6-7" fill="none" stroke="#fff" stroke-width="2"/></svg>
        <span>Admission Kit</span>
      </a>
      <a class="quick-link">
        <svg width="24" height="18" viewBox="0 0 24 18"><rect x="1" y="1" width="22" height="16" fill="#fff"/><path d="M1 1l11 9 11-9" fill="none" stroke="#7b65b3" stroke-width="2"/></svg>
        <span>Contact Us</span>
      </a>
    </div>
  </div>
  <main class="content-area">
    <article class="intro-panel">
      <h1>Welcome to The TM Home</h1>
      <p class="welcome-text">We are an Aged Care Facility that has been providing quality care and accommodation to the Brisbane community for over twenty years.</p>
      <p class="welcome-text">From this site you can learn more about us, find out all the types of accommodation available, what our Philosophy of Care is, send a message to a resident, contact us to request more information or download a brochure or an application form.</p>
    </article>
    <aside class="sidebar">
      <h2 class="sidebar-title">Accommodations</h2>
      <div class="room-card" style="top:93px"><div class="room-thumb" role="img" aria-label="Photo of a house with garden"></div><a>Accommodation Upper TM Nursing Suites (High Care)</a></div>
      <div class="room-card" style="top:195px"><div class="room-thumb" role="img" aria-label="Photo of the garden wing building"></div><a>Garden Wing &amp; Hibiscus Wing (Dementia Specific low care).</a></div>
      <div class="room-card" style="top:297px"><div class="room-thumb" role="img" aria-label="Photo of a white cottage unit"></div><a>TM Unit &amp; Tanner Wing (Frail Aged low care)</a></div>
      <a class="view-more" style="top:399px">view more</a>
    </aside>
  </main>
  <footer class="site-footer">Copyright 2009. TMhome</footer>
</section>

<!-- Content page -->
<section class="page page--content">
  <header class="site-header">
    <div class="brand"><span class="brand-mark"></span><span class="brand-name">THE TM HOME</span></div>
    <div class="phone">
      <svg width="24" height="24" viewBox="0 0 24 24"><path d="M6.6 10.8c1.4 2.8 3.8 5.1 6.6 6.6l2.2-2.2c.3-.3.7-.4 1-.2 1.1.4 2.3.6 3.6.6.6 0 1 .4 1 1V20c0 .6-.4 1-1 1C10.6 21 3 13.4 3 4c0-.6.4-1 1-1h3.5c.6 0 1 .4 1 1 0 1.3.2 2.5.6 3.6.1.3 0 .7-.2 1z" fill="#36304f"/></svg>
      07 5281 6637
    </div>
    <div class="utility-links">| Career Opportunity | &nbsp;Link &nbsp;| &nbsp;Contact Us &nbsp;|</div>
  </header>
  <nav class="main-nav">
    <a style="width:67px">Home</a>
    <a style="width:87px">About Us</a>
    <a class="is-current" style="width:146px">Accommodation</a>
    <a style="width:120px">Financial Info</a>
    <a style="width:158px">Philosophy of Care</a>
    <a style="width:108px">Contact Us</a>
    <a style="width:205px">Health &amp; Fitness Programs</a>
    <a class="newsletter" style="width:201px">Sign up for newsletter</a>
  </nav>
  <div class="hero">
    <div class="hero-photo" role="img" aria-label="Banner photo of an elderly couple sharing an affectionate moment"></div>
    <div class="quick-links">
      <a class="quick-link is-primary">
        <svg width="20" height="24" viewBox="0 0 22 26"><path d="M2 1h12l6 6v18H2z" fill="none" stroke="#fff" stroke-width="2"/><path d="M11 9v9M7 14l4 4 4-4" fill="none" stroke="#fff" stroke-width="2"/></svg>
        <span>Download<br>Application Form</span>
      </a>
      <a class="quick-link">
        <svg width="20" height="24" viewBox="0 0 22 26"><path d="M2 1h12l6 6v18H2z" fill="none" stroke="#fff" stroke-width="2"/><path d="M6 14l4 4 6-7" fill="none" stroke="#fff" stroke-width="2"/></svg>
        <span>Admission Kit</span>
      </a>
      <a class="quick-link">
        <svg width="22" height="16" viewBox="0 0 24 18"><rect x="1" y="1" width="22" height="16" fill="#fff"/><path d="M1 1l11 9 11-9" fill="none" stroke="#7b65b3" stroke-width="2"/></svg>
        <span>Contact Us</span>
      </a>
    </div>
  </div>
  <main class="content-area">
    <article class="intro-panel">
      <h1 class="section-title">
        <svg width="30" height="30" viewBox="0 0 30 30"><rect x="0" y="0" width="18" height="18" fill="#b3a6d6"/><rect x="10" y="10" width="18" height="18" fill="#7b65b3"/></svg>
        Accommodations
      </h1>
      <p class="body-text">The TM Home, situated in the riverside Brisbane Suburb of Riverbend, has a long history of providing accommodation to people of the community. The Riverbend Hostel, as it was known during World War II, was completely rebuilt in 1979 when the Senior Residents Welfare Association was formed.</p>
      <p class="body-text">Over the years refurbishments and renovations to the home have resulted in the establishment of a modern, comfortable facility which is a registered charitable organization, aligned to no other group and is administered by a voluntary board of directors.</p>
      <p class="body-text">The facility, on the corner of Harbour Street and Elm Street, Riverbend is surrounded by beautiful gardens and has many outdoor areas for recreation and relaxation.</p>
    </article>
    <aside class="sidebar">
      <h2 class="sidebar-title">Accommodations</h2>
      <div class="room-card" style="top:137px"><div class="room-thumb" role="img" aria-label="Photo of a house with garden"></div><a>Accommodation Upper TM Nursing Suites (High Care)</a></div>
      <div class="room-card" style="top:240px"><div class="room-thumb" role="img" aria-label="Photo of the garden wing building"></div><a>Garden Wing &amp; Hibiscus Wing (Dementia Specific low care).</a></div>
      <div class="room-card" style="top:343px"><div class="room-thumb" role="img" aria-label="Photo of a white cottage unit"></div><a>TM Unit &amp; Tanner Wing (Frail Aged low care)</a></div>
      <a class="view-more" style="top:444px">view more</a>
    </aside>
  </main>
  <footer class="site-footer">Copyright 2009. TMhome</footer>
</section>

</body>
</html>
```